Infographic for CPA Firm Lead Magnet

I need a one page infographic for a lead magnet for my CPA firm. The name of the lead magnet will be "G*** Most Owners Never Hand Their Bookkeeper". The lead magnet will need to have my firm logo (attached) on it, or watermarked on it. The attached Excel file has the three content categories which are the content basis for the infographic. My website is larkfieldtax.com to give you a better sense of my branding. Feel free to use whichever logo version you think is appropriate, and to take whatever information you deem appropriate from my website.

Target Market(s)

Business owners/entrepreneurs

Industry/Entity Type

Accounting

Font styles to use
Sans Serif

Colors

Designer to choose colors to be used in the design.

Requirements
Must have
• Must have each category and item listed on the Excel file. Must also have my logo or my logo watermarked.

```html
<!DOCTYPE html>
<html lang="en">
<head>
<meta charset="utf-8">
<title>CPA firm Infographic</title>
<link rel="stylesheet" href="https://fonts.googleapis.com/css2?family=Fira+Sans:wght@400;500;600&display=swap">
<style>
  :root{
    --sky:#D6EBFE;
    --cyan:#00C8FA;
    --azure:#0096FF;
    --ocean:#0A7ECF;
    --navy:#0A3A6B;
    --white:#FFFFFF;
    --mark:rgba(255,255,255,0.16);
  }
  *{margin:0;padding:0;box-sizing:border-box}
  html,body{width:1200px;height:981px;overflow:hidden;background:var(--sky)}
  body{font-family:"Fira Sans",Arial,sans-serif;color:var(--white)}
  .canvas{position:relative;width:1200px;height:981px;overflow:hidden}
  .shapes{position:absolute;left:0;top:0;width:1200px;height:981px}
  .shape-known{fill:var(--cyan)}
  .shape-maybe{fill:var(--azure)}
  .shape-discover{fill:var(--ocean)}

  .figure-area{position:absolute;left:266px;top:672px;width:338px;height:309px;background:var(--navy)}

  .title{position:absolute;left:70px;top:84px;color:var(--navy)}
  .title h1{font-size:46px;font-weight:600;line-height:1;letter-spacing:0.5px}
  .title p{font-size:24px;font-weight:400;margin-top:12px;letter-spacing:0.5px}

  .group{position:absolute;text-align:center;transform:translateX(-50%)}
  .group h2{font-weight:400;white-space:nowrap}
  .group ul{list-style:none}
  .group li{font-size:13.6px;line-height:28.8px;white-space:nowrap;font-weight:400}

  .group-known{left:134px;top:459px}
  .group-known h2{font-size:25.6px;line-height:29.6px}
  .group-known ul{margin-top:11px}

  .group-maybe{left:383px;top:327px}
  .group-maybe h2{font-size:25.6px;line-height:29.6px}
  .group-maybe ul{margin-top:35px}

  .group-discover h2{position:absolute;left:862px;top:143px;transform:translateX(-50%);font-size:32px;line-height:36.8px;text-align:center;white-space:nowrap;font-weight:400}
  .question-mark{position:absolute;left:874px;top:232px;transform:translateX(-50%);font-size:300px;font-weight:500;line-height:1;color:var(--mark)}
  .list-col{position:absolute;top:242px;transform:translateX(-50%);text-align:center;list-style:none}
  .list-col li{font-size:13.6px;line-height:28.8px;white-space:nowrap}
  .list-col-a{left:732px}
  .list-col-b{left:1010px}

  .brand{position:absolute;left:938px;top:825px;width:212px;height:89px;background:var(--white);display:flex;flex-direction:column;align-items:center;justify-content:center;color:var(--navy);font-weight:600;text-align:center}
  .brand-name{font-size:30px;line-height:1;letter-spacing:1px}
  .brand-sub{font-size:14px;letter-spacing:3px;margin-top:6px}
</style>
</head>
<body>
<main class="canvas">
  <svg class="shapes" viewBox="0 0 1500 1226" aria-hidden="true">
    <path class="shape-known" d="M465 850 L430 835 C420 810 400 800 330 795 C260 790 210 825 150 825 C60 825 0 760 0 680 C0 580 70 495 160 495 C210 495 250 515 270 540 C330 620 420 740 465 850 Z"/>
    <path class="shape-maybe" d="M465 850 C420 750 360 660 300 580 C260 530 245 490 245 450 C245 330 360 275 510 275 C640 275 700 330 705 410 C710 520 620 680 525 852 Z"/>
    <path class="shape-discover" d="M525 852 C600 700 650 560 695 350 C740 250 820 130 1000 105 C1100 95 1250 100 1380 130 C1470 160 1500 280 1500 400 C1500 560 1480 650 1450 740 C1410 820 1350 850 1270 850 C1150 850 1000 770 800 790 C760 795 730 815 710 835 Z"/>
  </svg>

  <div class="figure-area" role="img" aria-label="Silhouette of a head in profile from which the thought bubbles rise"></div>

  <header class="title">
    <h1>CPA firm</h1>
    <p>Infographic</p>
  </header>

  <section class="group group-known">
    <h2>Things You<br>Already Know</h2>
    <ul>
      <li>Accounting &amp; Bookkeeping</li>
      <li>Federal Taxes</li>
      <li>State Taxes</li>
    </ul>
  </section>

  <section class="group group-maybe">
    <h2>Things You<br>May Know</h2>
    <ul>
      <li>1099 Issuance</li>
      <li>Financial Planning</li>
      <li>IRS Resolution</li>
      <li>Payroll</li>
      <li>Tax Planning</li>
    </ul>
  </section>

  <section class="group-discover">
    <span class="question-mark" aria-hidden="true">?</span>
    <h2>But Did<br>You Know?</h2>
    <ul class="list-col list-col-a">
      <li>Benchmarking</li>
      <li>Budgeting</li>
      <li>Business Acquisition Due Diligence</li>
      <li>Business Management Reports</li>
      <li>Business Plans</li>
      <li>Business Strategy Consulting</li>
      <li>Business Valuation</li>
      <li>Cash Flow Management</li>
      <li>Choice of Legal Structure Consulting</li>
      <li>Dashboards</li>
      <li>Divorce Consulting</li>
    </ul>
    <ul class="list-col list-col-b">
      <li>Financial Forecasting</li>
      <li>Internal Controls Consulting</li>
      <li>Key Performance Indicator Development</li>
      <li>Local Taxes</li>
      <li>Payroll Tax Returns</li>
      <li>Performance Tracking</li>
      <li>Profitability Analysis</li>
      <li>Sales Tax Returns</li>
      <li>Software Consulting &amp; Implementation</li>
      <li>Succession Planning</li>
    </ul>
  </section>

  <div class="brand">
    <span class="brand-name">LARKFIELD</span>
    <span class="brand-sub">TAX</span>
  </div>
</main>
</body>
</html>
```